Marrowfen Vodka label redesign

This label was originally screen-printed. I would like it redesigned to fit a new rectangular paper label that will cover the screen-printed label of a different bottle than what was previously earmarked for a different product. I can easily resize the elements from the original label to fit the new size, but I would like to see some creative options for the new size. Show me what you've got!
Here are some guidelines:
New label must contain the butterfly and text "Marrowfen" in its existing font (that's our logo) the color is optional. It must also contain the barcode and all other text elements but font, style, size and color can change:
The Government warning text cannot be smaller. Style and font cannot change, but the justification can change.
The filigree does not have to stay.
The previous label was broken up into 3 panels. The new label will be one solid label encircling the bottle. The label size will be 10.5" x 5.5" (266.7 mm x 139.7 mm) AI template attached.

Target Market(s)

Women age 35 and up with disposable income

Font styles to use
Other font styles liked:
• Mostra Nuova

Colors

Designer to choose colors to be used in the design.

Requirements
Must have
• Class
Nice to have
• ArtDeco elements
Should not have
• Sharp edges

```html
<!DOCTYPE html>
<html lang="en">
<head>
<meta charset="utf-8">
<title>Marrowfen Vodka – Wraparound Label</title>
<link rel="stylesheet" href="https://fonts.googleapis.com/css2?family=Cherry+Swash:wght@700&family=Arvo:ital,wght@0,700;1,700&family=Lora:wght@400;600&display=swap">
<style>
  :root {
    --backdrop: #f1f2f4;
    --label-deep: #33268e;
    --label-mid: #4636a8;
    --label-edge: #2a1f7a;
    --accent-sky: #7fd4ea;
    --accent-pale: #bfeaf5;
    --text-light: #eef0ff;
    --panel-rule: rgba(127, 212, 234, 0.28);
    --code-field: #ffffff;
  }
  * { box-sizing: border-box; margin: 0; padding: 0; }
  html, body {
    width: 1200px;
    height: 900px;
    overflow: hidden;
    background: var(--backdrop);
  }
  .canvas {
    width: 1200px;
    height: 900px;
    display: flex;
    align-items: center;
    justify-content: center;
  }
  .label {
    width: 1100px;
    height: 576px;
    border-radius: 14px;
    background: linear-gradient(90deg, var(--label-edge) 0%, var(--label-mid) 18%, var(--label-deep) 50%, var(--label-mid) 82%, var(--label-edge) 100%);
    display: grid;
    grid-template-columns: 1fr 1fr 1fr;
    position: relative;
    overflow: hidden;
    color: var(--text-light);
  }
  .label::before, .label::after {
    content: "";
    position: absolute;
    left: 24px; right: 24px;
    height: 2px;
    background: var(--panel-rule);
    border-radius: 2px;
  }
  .label::before { top: 18px; }
  .label::after { bottom: 18px; }
  .panel {
    padding: 56px 40px;
    position: relative;
  }
  .panel + .panel { border-left: 1px solid var(--panel-rule); }

  /* Story panel */
  .story {
    font-family: "Lora", serif;
    font-size: 12.5px;
    line-height: 1.55;
    text-align: justify;
    display: flex;
    flex-direction: column;
    justify-content: center;
    gap: 18px;
  }
  .barcode-field {
    width: 92px;
    height: 52px;
    border-radius: 4px;
    background: var(--code-field);
  }

  /* Brand panel */
  .brand {
    display: flex;
    flex-direction: column;
    align-items: center;
    text-align: center;
    padding-top: 44px;
  }
  .brand-mark {
    width: 84px;
    height: 84px;
    border-radius: 50%;
    background: var(--accent-sky);
    margin-bottom: 14px;
  }
  .brand-name {
    font-family: "Cherry Swash", serif;
    font-weight: 700;
    font-size: 58px;
    line-height: 1;
    color: var(--accent-sky);
  }
  .brand-line {
    font-family: "Arvo", serif;
    font-weight: 700;
    font-style: italic;
    font-size: 30px;
    line-height: 1.05;
    color: var(--accent-pale);
    margin-top: 12px;
  }
  .brand-facts {
    font-family: "Lora", serif;
    font-weight: 600;
    font-size: 14px;
    line-height: 1.45;
    margin-top: 20px;
  }
  .product-banner {
    margin-top: 26px;
    width: 250px;
    position: relative;
  }
  .product-banner svg { display: block; }
  .product-type {
    position: absolute;
    inset: 0;
    display: flex;
    align-items: center;
    justify-content: center;
    font-family: "Arvo", serif;
    font-weight: 700;
    font-size: 30px;
    letter-spacing: 3px;
    color: var(--accent-pale);
  }

  /* Legal panel */
  .legal {
    font-family: "Lora", serif;
    font-size: 12.5px;
    line-height: 1.5;
    display: flex;
    flex-direction: column;
    justify-content: center;
    gap: 18px;
  }
  .warning { text-align: justify; }
  .warning-head { font-weight: 600; letter-spacing: 0.5px; }
  .distill { text-align: center; }
  .site { text-align: center; font-weight: 600; }
  .tagline {
    text-align: center;
    font-family: "Cherry Swash", serif;
    font-weight: 700;
    font-size: 22px;
    color: var(--accent-sky);
  }
</style>
</head>
<body>
<main class="canvas">
  <section class="label" aria-label="Marrowfen Vodka wraparound label">
    <div class="panel story">
      <p>Marrowfen Spirits is an Oregon grown company located in the heart of the Willamette Valley with the goal of providing authentic, hand-crafted, artisan spirits using as many locally sourced products as possible. The Marrowfen butterfly is Oregon's state insect. For us it means delicate, light and, like the butterfly, through much effort our vodka became something beautiful. We produce our vodka in small batches and it's blended with pristine Willamette River water that has not only been filtered through the Northwest's unique volcanic geology, but our proprietary system as well. The finished product has been filtered five times through activated carbon for an incredibly clean, smooth finish.</p>
      <div class="barcode-field" role="img" aria-label="Product barcode area"></div>
    </div>

    <div class="panel brand">
      <div class="brand-mark" role="img" aria-label="Butterfly emblem"></div>
      <h1 class="brand-name">Marrowfen</h1>
      <p class="brand-line">Small-batch<br>Premium</p>
      <p class="brand-facts">Alcohol 40% by volume (80 Proof)<br>750ml<br>made in Willamette Valley, Oregon, USA</p>
      <div class="product-banner">
        <svg width="250" height="64" viewBox="0 0 250 64" aria-hidden="true">
          <line x1="0" y1="32" x2="34" y2="32" stroke="#7fd4ea" stroke-width="2" stroke-linecap="round"/>
          <line x1="216" y1="32" x2="250" y2="32" stroke="#7fd4ea" stroke-width="2" stroke-linecap="round"/>
          <rect x="36" y="8" width="178" height="48" rx="10" fill="none" stroke="#7fd4ea" stroke-width="2.5"/>
          <rect x="42" y="14" width="166" height="36" rx="7" fill="none" stroke="#7fd4ea" stroke-width="1"/>
        </svg>
        <span class="product-type">VODKA</span>
      </div>
    </div>

    <div class="panel legal">
      <p class="warning"><span class="warning-head">GOVERNMENT WARNING:</span> (1) According to the Surgeon General, women should not drink alcoholic beverages during pregnancy because of the risk of birth defects. (2) Consumption of alcoholic beverages impairs your ability to drive a car or operate machinery, and may cause health problems.</p>
      <p class="distill">Neutral Grain Spirits distilled from corn<br>Produced and bottled by Marrowfen Spirits, Salem, OR</p>
      <p class="site">www.marrowfenspirits.com</p>
      <p class="tagline">Savor Slowly</p>
    </div>
  </section>
</main>
</body>
</html>
```